Flyer-Design für Beratungsunternehmen
Vielen Dank für die professionelle und überdurchschnittliche Unterstützung
Zielgruppe
Supervision, Coaching, Beratung
Plus digitale Beratung via App, sonstiger moderner Medien
für Organisationen, Firmen, Institutionen, Privatpersonen
Aufgabenstellung
Kreatives Design, modern, hochwertig
symphatisch, vertrauensvoll, transparent, ansprechend
Texte, Inhalte und Bilder siehe download
Sehr wichtig corporate design laut homepage www.reflexionamufer.de

```html
<!DOCTYPE html>
<html lang="de">
<head>
<meta charset="utf-8">
<title>Reflexion am Ufer – Flyer</title>
<link rel="stylesheet" href="https://fonts.googleapis.com/css2?family=Roboto+Condensed:wght@300;400;700&family=Raleway:wght@400;500;700&display=swap">
<style>
:root{
  --green:#8fc824;
  --green-light:#a3d33a;
  --orange:#e4701e;
  --dark:#2b2b2b;
  --text:#4a4a4a;
  --paper-grey:#ececec;
  --paper-white:#f8f8f8;
  --stage:#e3e3e3;
}
*{box-sizing:border-box;margin:0;padding:0}
html,body{width:905px;height:1200px;overflow:hidden}
body{background:var(--stage);font-family:"Raleway",sans-serif;color:var(--text);position:relative}
.spread{position:absolute;left:22px;width:860px;height:462px;overflow:hidden;box-shadow:0 8px 18px rgba(0,0,0,.15)}
.spread--outer{top:50px}
.spread--inner{top:650px;height:455px}
.panel{position:absolute;top:0;width:430px;height:100%;overflow:hidden}
.panel--left{left:0}
.panel--right{left:430px}
.abs{position:absolute}
.heading-font{font-family:"Roboto Condensed",sans-serif}

/* outer */
.photo-portrait{left:0;top:0;width:430px;height:300px;background:linear-gradient(135deg,#c9d3d6 0%,#9fb0b6 45%,#6d7b80 100%)}
.photo-dandelion{left:0;top:0;width:430px;height:300px;background:radial-gradient(circle at 40% 40%,#ffffff 0%,#eef3ef 25%,#bfe3dc 55%,#f1e7b6 85%,#f4eedc 100%)}
.wave{left:0;top:0}
.badge{left:264px;top:220px;width:96px;height:96px;border-radius:50%;background:var(--orange);border:3px solid #cfe6a5;display:flex;align-items:center;justify-content:center;text-align:center;transform:rotate(-8deg);color:#fff;font-family:"Roboto Condensed",sans-serif;font-size:13.5px;line-height:15px;font-weight:400}
.contact{color:#fff;font-size:8.2px;line-height:11px}
.contact .label{font-family:"Roboto Condensed",sans-serif;font-size:8.5px}
.contact strong{font-weight:700}
.contact .web{font-weight:700;font-size:8.8px}
.brand{display:flex;align-items:center;gap:6px;font-family:"Roboto Condensed",sans-serif;font-weight:400;white-space:nowrap}
.brand-mark{width:12px;height:12px;background:var(--green)}
.brand--white{color:#fff;font-size:14px}
.brand--white .brand-mark{background:#fff}
.brand--dark{color:var(--dark);font-size:14px}
.quote{left:72px;top:322px;width:330px;color:#fff;font-family:"Roboto Condensed",sans-serif;font-weight:300;font-size:19.5px;line-height:27px;letter-spacing:.2px}
.quote-source{right:50px;top:420px;color:#fff;font-family:"Roboto Condensed",sans-serif;font-size:8.6px}

/* inner */
.panel--grey{background:var(--paper-grey)}
.panel--white{background:var(--paper-white)}
.logo-disc{left:-4px;top:-44px;width:150px;height:150px;border-radius:50%;background:#f4f4f4;box-shadow:0 2px 6px rgba(0,0,0,.15);display:flex;align-items:flex-end;justify-content:center;padding-bottom:38px}
.photo-circle{border-radius:50%;border:3px solid #fff;box-shadow:0 2px 6px rgba(0,0,0,.18)}
.photo-laptop{left:364px;top:-8px;width:128px;height:128px;background:linear-gradient(160deg,#dfe6ea 0%,#9fb0b8 50%,#2f3b57 100%)}
.photo-lake{left:-82px;top:352px;width:156px;height:156px;background:linear-gradient(180deg,#f3d6a0 0%,#c7a67a 45%,#7d6a55 100%)}
.photo-lake--right{left:348px;top:352px;width:156px;height:156px}
.col{position:absolute;font-size:7.3px;line-height:10px}
.h-orange{font-family:"Roboto Condensed",sans-serif;font-weight:700;color:var(--orange);font-size:12.5px;line-height:15px;margin-bottom:12px}
.h-green{font-family:"Roboto Condensed",sans-serif;font-weight:400;color:var(--green);font-size:10.5px;line-height:12px;margin-bottom:5px}
.h-small{font-size:8.5px;color:var(--dark);margin:10px 0 3px}
.col p{margin-bottom:14px}
.checks{list-style:none}
.checks li{position:relative;padding-left:12px;margin-bottom:5px}
.checks li::before{content:"✔";position:absolute;left:0;top:0;color:var(--orange);font-size:7.5px}
.checks--sub{margin-left:12px;margin-top:4px}
.checks--sub li::before{color:var(--green)}
.checks--tight li{margin-bottom:4px}
.two-col{display:flex;gap:20px}
</style>
</head>
<body>

<!-- Außenseite -->
<section class="spread spread--outer">
  <div class="panel panel--left" style="background:var(--green)">
    <div class="abs photo-portrait" role="img" aria-label="Porträtfoto der Beraterin vor einer Glasfassade"></div>
    <svg class="abs wave" width="430" height="462" viewBox="0 0 430 462">
      <path d="M0 282 Q200 268 430 285 L430 462 L0 462 Z" fill="#fff" opacity=".85"/>
      <path d="M0 292 Q200 276 430 292 L430 462 L0 462 Z" fill="var(--green)"/>
    </svg>
    <div class="abs badge">ICH FREUE<br>MICH AUF<br>SIE!</div>
    <div class="abs contact" style="left:28px;top:353px">
      <div class="label">KONTAKT</div>
      <div style="margin-top:8px"><strong>REFLEXION AM UFER</strong><br>Lena Burkhard</div>
      <div style="margin-top:12px">Uferweg 12<br>65000 Lindental am Main</div>
    </div>
    <div class="abs contact" style="left:140px;top:373px">
      <div>Telefon:&nbsp; +49 (0)160 555 01 42<br>E-Mail:&nbsp;&nbsp; info@reflexionamufer.de</div>
      <div style="margin-top:12px">Web:<br><span class="web">www.reflexionamufer.de</span></div>
    </div>
    <div class="abs brand brand--white" style="left:290px;top:412px"><span class="brand-mark"></span>REFLEXION AM UFER</div>
  </div>

  <div class="panel panel--right" style="background:var(--green)">
    <div class="abs photo-dandelion" role="img" aria-label="Pusteblume vor hellem, unscharfem Frühlingshintergrund"></div>
    <svg class="abs wave" width="430" height="462" viewBox="0 0 430 462">
      <path d="M0 270 Q220 228 430 218 L430 462 L0 462 Z" fill="#fff" opacity=".55"/>
      <path d="M0 285 Q220 262 430 252 L430 462 L0 462 Z" fill="var(--green)"/>
    </svg>
    <div class="abs brand brand--dark" style="left:272px;top:78px"><span class="brand-mark"></span>REFLEXION AM UFER</div>
    <blockquote class="abs quote">„ES IST NICHT ZU WENIG ZEIT DIE WIR HABEN, SONDERN ES IST ZU VIEL ZEIT, DIE WIR NICHT NUTZEN.“</blockquote>
    <div class="abs quote-source">Marcus Velten – Philosoph</div>
  </div>
</section>

<!-- Innenseite -->
<section class="spread spread--inner">
  <div class="panel panel--left panel--grey">
    <svg class="abs wave" width="430" height="455" viewBox="0 0 430 455">
      <path d="M120 62 Q280 88 430 90" stroke="#cfe6a5" stroke-width="5" fill="none"/>
    </svg>
    <div class="abs logo-disc"><div class="brand brand--dark" style="font-size:11px"><span class="brand-mark" style="width:10px;height:10px"></span>REFLEXION AM UFER</div></div>
    <div class="abs photo-circle photo-lake" style="left:292px;top:360px" role="img" aria-label="Frau meditiert auf einem Steg am See bei Sonnenaufgang"></div>

    <div class="col" style="left:32px;top:120px;width:165px">
      <div class="h-orange">MEINE FACHGEBIETE FÜR EIN BESSERES WOHLFÜHLEN</div>
      <div class="h-green">SYSTEMISCHE SUPERVISION</div>
      <p style="margin-bottom:0">Bietet Ihnen und Ihrem Team einen geschützten Raum Ihren Arbeitskontext, komplexe Anforderungen und Strukturen moderiert zu reflektieren sowie Konflikte, Rollen und Fragestellungen zu klären.</p>
      <div class="h-small">Ziele</div>
      <ul class="checks">
        <li>Rollensicherheit und Teamfähigkeit weiterentwickeln</li>
        <li>tiefes Verständnis der beruflichen Situation, Handlungsmöglichkeiten und Perspektiven entwickeln.</li>
        <li>Qualitätssicherung.</li>
        <li>Stärken &amp; Kompetenzen bewusst machen</li>
        <li>langfristig die Freude an Ihrer Arbeit erhalten
          <ul class="checks checks--sub checks--tight">
            <li>Einzelsupervision</li>
            <li>Gruppensupervision</li>
            <li>Teamsupervision</li>
            <li>Fallsupervision</li>
          </ul>
        </li>
      </ul>
    </div>

    <div class="col" style="left:226px;top:122px;width:170px">
      <div class="h-green">SYSTEMISCHES COACHING</div>
      <p style="margin-bottom:30px">Erweitern Sie Ihre beruflichen Handlungsstrategien und machen Sie Ihre Stärken und Fähigkeiten nutzbar, um Ihr Ziel zu erreichen. Persönliche Zufriedenheit und professionelle Leistungsfähigkeit stehen im Fokus.</p>
      <div class="h-green">LIFECOACHING</div>
      <p style="margin-bottom:20px">Im Mittelpunkt stehen Ihre persönlichen Sorgen, Wünsche und Anliegen.<br>Gemeinsam erarbeiten wir Ihr konkretes Ziel und gehen auf Schatzsuche, entdecken neue Perspektiven, Handlungsoptionen, die Sie Schritt für Schritt Ihrem persönlichen Erfolg näherbringen.</p>
      <div class="h-green">DIGITALE BERATUNG</div>
      <p>Endlich können Sie ganz einfach ungenutzte Zeit auf dem Weg zur Arbeit, in Wartebereichen oder Zwischendurch nutzen, um Ihre Ziele und Wünsche wahr werden zu lassen.</p>
    </div>
  </div>

  <div class="panel panel--right panel--white">
    <svg class="abs wave" width="430" height="455" viewBox="0 0 430 455">
      <path d="M0 90 Q200 82 300 38" stroke="#cfe6a5" stroke-width="5" fill="none"/>
    </svg>
    <div class="abs photo-circle" style="left:-78px;top:360px;width:156px;height:156px;background:linear-gradient(180deg,#f3d6a0 0%,#c7a67a 45%,#7d6a55 100%)" role="img" aria-label="Frau meditiert auf einem Steg am See bei Sonnenaufgang"></div>
    <div class="abs photo-circle photo-laptop" role="img" aria-label="Beraterin am Laptop in einem hellen Büro"></div>

    <div class="col" style="left:27px;top:122px;width:165px">
      <div class="h-orange" style="margin-bottom:8px">BEI MIR ERHALTEN SIE</div>
      <ul class="checks">
        <li>Eigenen geschützten Account / eigene App</li>
        <li>24 Stunden / 7 Tage in der Woche Zugang</li>
        <li>Visualisierung Ihrer Erfolge</li>
        <li>Eine Vielzahl an Tools und Fragebögen zur konkreten Umsetzungsbegleitung</li>
        <li>Responsive Design / nutzbar auf dem Smartphone, Tablet, PC</li>
        <li>Höchstmaß an Flexibilität</li>
        <li>Extrem effizient und dadurch zeit- und geldsparend</li>
        <li>Entscheiden Sie selbst, ob Sie die Möglichkeit der digitalen Beratung zusätzlich nutzen wollen oder diese die Sitzungen vor Ort komplett ersetzen soll.</li>
        <li>Sie möchten auf die klassischen Sitzungen nicht verzichten?</li>
        <li>Nutzen Sie die digitale Begleitung dazwischen und / oder nach dem gesamten Beratungsprozess (Follow-Up). So sichern Sie Ihre Erfolge auch langfristig und brauchen vor Herausforderungen und Widerständen im Alltag keine Angst mehr haben.</li>
      </ul>
    </div>

    <div class="col" style="left:219px;top:122px;width:195px">
      <div class="h-green">VORZÜGE</div>
      <div class="two-col">
        <ul class="checks checks--tight"><li>Effizienz,</li><li>Mobilität,</li><li>Flexibilität,</li><li>Nachhaltigkeit,</li></ul>
        <ul class="checks checks--tight"><li>Sicherheit,</li><li>größmögliche Anonymität.</li><li>Sparen Sie Zeit und Geld!</li></ul>
      </div>
      <div class="h-green" style="margin-top:14px">MEIN FORMAT FÜR IHREN MEHRWERT!</div>
      <ul class="checks">
        <li>Nachhaltiger Erfolg durch digitale Begleitung</li>
        <li>Der rote Faden der Veränderungsarbeit</li>
        <li>Beste Transfer- &amp; Nachbegleitung</li>
        <li>Zeit- &amp; Ortsunabhängiges Coaching</li>
      </ul>
      <div class="h-green" style="margin-top:14px">MEINE WERTE UND HALTUNG</div>
      <ul class="checks">
        <li>Wertschätzung, Ressourcenorientierung und Respekt</li>
        <li>Systemisch</li>
        <li>Lösungsorientiert</li>
        <li>Kompetenz und Methodenvielfalt</li>
        <li>Nicht für, sondern mit Ihnen!</li>
        <li>Transparenz und Struktur</li>
        <li>Verschwiegenheit und Vertrauen</li>
      </ul>
    </div>
  </div>
</section>

</body>
</html>
```